LanternPips business card for creator of IP TOY (fun) (children) designs

This business card will be the introduction of me as the creator of new designs to the toy industry and beyond. These designs are kept secret until being revealed one on one to each company. My design is patent pending protected IP. I am looking for business appropriate with a tinge of fun. Please no black backgounds as this is the toy industry. Be creative with the logo and colors please. Just imagine.

Target Market(s)

TOY Industry Executives - Inventor Relations - Manufacturers this is my first introduction card.

Industry/Entity Type

Toy Industry - I have included our Brand colors which can be seen on the cover of The Quiet Pebble Moon book so uses for any of these others colors would be intersting.

Contact Information for Business Card

LOGO Mara Delwyn Founder Creator 555 017 2869 4718 E Hollin Bend Anna, TX 70812 www.lanternpips-demo.com maradelwyn@quillpost-mail.com Patent Pending IP

Font styles to use
Other font styles liked:
• The font used in the logo is Swiss721BT bold I need to see other fonts to be able to decide but need a clean look

Requirements
Must have
• A bit of an artistic flair although the logo is very simple. I am in the toy industry so would like something that sparks the look of being a creator?
Nice to have
• Please try a background other than stark white. Would like to see a play using brand colors?I like the logos which look like they are lifted off the page. Then under the logo the words (not lifted?) Any Action Any Character Any Teaching
Should not have
• No Black Backgrounds please! should look as clean as possible - I am not opposed to changing to a double sided card if that is more effectual.

```html
<!DOCTYPE html>
<html lang="en">
<head>
<meta charset="utf-8">
<title>LanternPips Business Card</title>
<link href="https://fonts.googleapis.com/css2?family=Poppins:wght@400;500;700&display=swap" rel="stylesheet">
<style>
  :root {
    --page: #e4e6ea;
    --card: #fbf4e8;
    --card-edge: #f3e6d2;
    --card-deep: #ecdcc3;
    --red: #d62129;
    --ink: #3a2e2a;
    --ink-muted: #6e5f57;
  }
  * { box-sizing: border-box; margin: 0; padding: 0; }
  html, body {
    width: 1200px; height: 900px; overflow: hidden;
    background: var(--page);
    font-family: "Poppins", sans-serif;
  }
  .canvas {
    width: 1200px; height: 900px;
    display: flex; flex-direction: column; align-items: center; justify-content: center; gap: 40px;
  }
  .card {
    position: relative; width: 630px; height: 360px;
    background: linear-gradient(160deg, var(--card) 0%, var(--card-edge) 100%);
    border-radius: 26px;
    box-shadow: 0 14px 30px rgba(40, 30, 20, 0.16);
    overflow: hidden;
  }
  .card-front {
    display: flex; flex-direction: column; align-items: center; justify-content: center; gap: 14px;
  }
  .brand-name {
    font-weight: 700; font-size: 74px; letter-spacing: -1px;
    color: var(--red); line-height: 1;
  }
  .tagline {
    font-size: 15px; font-weight: 500; letter-spacing: 3px;
    text-transform: uppercase; color: var(--ink-muted);
  }
  .card-back .brand-name {
    position: absolute; left: 0; right: 0; top: 58px; text-align: center;
    color: var(--card-deep); font-size: 70px;
  }
  .person { position: absolute; left: 44px; top: 192px; }
  .person-name { color: var(--red); font-weight: 700; font-size: 25px; line-height: 1.1; }
  .person-title { color: var(--ink); font-size: 15px; margin-top: 3px; }
  .divider {
    position: absolute; left: 44px; right: 44px; top: 262px;
    height: 1px; background: var(--red);
  }
  .contact-list { position: absolute; left: 44px; top: 274px; list-style: none; }
  .contact-list li {
    display: flex; align-items: center; gap: 9px;
    color: var(--ink); font-size: 14px; line-height: 22px;
  }
  .contact-list svg { width: 12px; height: 12px; fill: var(--red); flex: none; }
  .address {
    position: absolute; right: 44px; top: 274px; text-align: right;
    color: var(--ink); font-size: 14px; line-height: 22px; font-style: normal;
  }
  .patent { color: var(--red); font-weight: 500; }
</style>
</head>
<body>
<main class="canvas">
  <section class="card card-front" aria-label="Card front">
    <h1 class="brand-name">LanternPips</h1>
    <p class="tagline">Any Action · Any Character · Any Teaching</p>
  </section>

  <section class="card card-back" aria-label="Card back">
    <p class="brand-name">LanternPips</p>

    <div class="person">
      <h2 class="person-name">Mara Delwyn</h2>
      <p class="person-title">Founder &amp; Creator</p>
    </div>

    <div class="divider"></div>

    <ul class="contact-list">
      <li>
        <svg viewBox="0 0 24 24" aria-hidden="true"><path d="M6.6 10.8a15.1 15.1 0 0 0 6.6 6.6l2.2-2.2c.3-.3.7-.4 1-.2 1.1.4 2.3.6 3.6.6.6 0 1 .4 1 1V20c0 .6-.4 1-1 1A17 17 0 0 1 3 4c0-.6.4-1 1-1h3.5c.6 0 1 .4 1 1 0 1.3.2 2.5.6 3.6.1.3 0 .7-.2 1l-2.3 2.2z"/></svg>
        555 017 2869
      </li>
      <li>
        <svg viewBox="0 0 24 24" aria-hidden="true"><path d="M2 5h20v2l-10 6L2 7zM2 9l10 6 10-6v10H2z"/></svg>
        maradelwyn@quillpost-mail.com
      </li>
      <li>
        <svg viewBox="0 0 24 24" aria-hidden="true"><path d="M12 2a10 10 0 1 0 0 20 10 10 0 0 0 0-20zm0 2c.9 0 2.3 2 2.8 5H9.2C9.7 6 11.1 4 12 4zm-8 8c0-.7.1-1.4.3-2h3c-.1.7-.1 1.3-.1 2s0 1.3.1 2h-3c-.2-.6-.3-1.3-.3-2zm5.2 3h5.6c-.5 3-1.9 5-2.8 5s-2.3-2-2.8-5zm7.5-1c.1-.7.1-1.3.1-2s0-1.3-.1-2h3c.2.6.3 1.3.3 2s-.1 1.4-.3 2z"/></svg>
        www.lanternpips-demo.com
      </li>
    </ul>

    <address class="address">
      4718 E Hollin Bend<br>
      Anna, TX 70812<br>
      <span class="patent">Patent Pending IP</span>
    </address>
  </section>
</main>
</body>
</html>
```